Pharmacist turned chef in Key West Fl needs a logo design

I am looking for a professional looking business card that says who I am and what I do. For example Chef Dale Morvik, natural organic and health supportive cooking. Phone 555-416-8870 email dalemorvik@quillpost.example web www.thesaltedharvest.example, Key West fl. The color or colors should have some green and other colors that look good together that stimulate appetite and give a clean healthy image. To help with a thought process, words like food as medicine, medicine is food, good nutrition is health but at the same time I do not want a lot of medical symbols that me it look clinical. Any questions please contact me.

```html
<!DOCTYPE html>
<html lang="en">
<head>
<meta charset="utf-8">
<title>Chef Dale Morvik — Business Card</title>
<link rel="stylesheet" href="https://fonts.googleapis.com/css2?family=Open+Sans:wght@400;700&display=swap">
<style>
  :root {
    --page: #ffffff;
    --frame: #222222;
    --card-green: #b0c905;
    --band: #ffffff;
    --ink: #1e1e1e;
    --leaf-green: #4fae3a;
    --mark-green: #5cb33f;
    --icon-bg: #ffffff;
  }
  html, body {
    margin: 0;
    padding: 0;
    width: 1200px;
    height: 781px;
    overflow: hidden;
    background: var(--page);
    font-family: "Open Sans", Arial, sans-serif;
  }
  .sheet {
    position: relative;
    width: 1200px;
    height: 781px;
    box-sizing: border-box;
    border: 2px solid var(--frame);
    background: var(--page);
  }
  .card {
    position: absolute;
    left: 56px;
    top: 55px;
    width: 1087px;
    height: 670px;
    box-sizing: border-box;
    border: 2px solid var(--frame);
    background: var(--card-green);
  }
  .tagline-band {
    position: absolute;
    left: 0;
    right: 0;
    top: 166px;
    height: 168px;
    background: var(--band);
  }
  .brand-mark {
    position: absolute;
    left: 112px;
    top: 24px;
    width: 112px;
    height: 112px;
    border-radius: 50%;
    background: var(--mark-green);
  }
  .tagline {
    position: absolute;
    left: 244px;
    top: 38px;
    margin: 0;
    font-weight: 400;
    line-height: 1;
  }
  .tagline-lead {
    display: block;
    font-size: 44px;
    font-weight: 400;
    color: var(--ink);
    letter-spacing: 0.2px;
  }
  .tagline-focus {
    display: block;
    margin-top: 12px;
    font-size: 44px;
    font-weight: 700;
    color: var(--leaf-green);
  }
  .chef-name {
    position: absolute;
    left: 62px;
    top: 430px;
    margin: 0;
    font-size: 37px;
    font-weight: 700;
    color: var(--ink);
    line-height: 1;
  }
  .contact-list {
    position: absolute;
    left: 451px;
    top: 441px;
    margin: 0;
    padding: 0;
    list-style: none;
  }
  .contact-item {
    display: flex;
    align-items: center;
    height: 35px;
    margin-bottom: 32px;
    font-size: 33px;
    color: var(--ink);
  }
  .contact-icon {
    width: 35px;
    height: 35px;
    margin-right: 24px;
    border-radius: 6px;
    background: var(--icon-bg);
    flex: none;
  }
</style>
</head>
<body>
  <div class="sheet">
    <section class="card">
      <div class="tagline-band">
        <div class="brand-mark" role="img" aria-label="Chef brand mark"></div>
        <h1 class="tagline">
          <span class="tagline-lead">NATURAL ORGANIC AND</span>
          <span class="tagline-focus">HEALTH SUPPORTIVE COOKING</span>
        </h1>
      </div>

      <h2 class="chef-name">Chef Dale Morvik</h2>

      <ul class="contact-list">
        <li class="contact-item">
          <svg class="contact-icon" viewBox="0 0 35 35" aria-hidden="true">
            <path d="M13 8 L16 12 L14 15 C15 18 17 21 20 22 L23 20 L27 23 L25 27 C18 27 11 19 10 11 Z" fill="none" stroke="#1e1e1e" stroke-width="2" stroke-linejoin="round"/>
          </svg>
          <span>555-416-8870</span>
        </li>
        <li class="contact-item">
          <svg class="contact-icon" viewBox="0 0 35 35" aria-hidden="true">
            <rect x="7" y="10" width="21" height="15" fill="#1e1e1e"/>
            <path d="M7 10 L17.5 19 L28 10" fill="none" stroke="#ffffff" stroke-width="1.6"/>
          </svg>
          <span>dalemorvik@quillpost.example</span>
        </li>
        <li class="contact-item">
          <svg class="contact-icon" viewBox="0 0 35 35" aria-hidden="true">
            <g fill="none" stroke="#1e1e1e" stroke-width="1.4">
              <circle cx="17.5" cy="17.5" r="10"/>
              <ellipse cx="17.5" cy="17.5" rx="4.5" ry="10"/>
              <line x1="7.5" y1="17.5" x2="27.5" y2="17.5"/>
              <line x1="17.5" y1="7.5" x2="17.5" y2="27.5"/>
              <path d="M9.5 12 H25.5 M9.5 23 H25.5"/>
            </g>
          </svg>
          <span>www.thesaltedharvest.example</span>
        </li>
      </ul>
    </section>
  </div>
</body>
</html>
```